" A Vitralis é uma empresa que atua na área da saúde e realiza atividade de comercializaçao de equipamentos médicos, voltados na sua maioria para àrea laboratorial. Possuimos um site que está desatualizado www.vitralis-exemplo.com.br. Aprovamos uma nova logo recentemente. "

```html
<!DOCTYPE html>
<html lang="pt-BR">
<head>
<meta charset="utf-8">
<title>Vitralis</title>
<link href="https://fonts.googleapis.com/css2?family=Open+Sans:wght@300;400;600;700&display=swap" rel="stylesheet">
<style>
:root{
  --red:#c8161d;
  --ink:#3c3c3c;
  --muted:#8a8a8a;
  --line:#e2e2e2;
  --panel:#ffffff;
  --bg-top:#ffffff;
  --bg-gray:#d6d6d6;
  --footer:#4a4a4a;
  --footer-text:#e6e6e6;
  --hero-a:#6f8b9a;
  --hero-b:#b7c8d1;
  --btn:#3d3d3d;
}
*{box-sizing:border-box;margin:0;padding:0}
html,body{width:1200px;height:1200px;overflow:hidden}
body{font-family:"Open Sans",Arial,sans-serif;color:var(--ink);position:relative;
  background:linear-gradient(180deg,var(--bg-top) 0,var(--bg-top) 190px,#ececec 330px,var(--bg-gray) 700px,#e4e4e4 960px);}
.abs{position:absolute}

.brand{left:252px;top:40px;display:flex;align-items:center;gap:12px}
.brand-dot{width:34px;height:34px;border-radius:50%;background:var(--red)}
.brand-name{font-size:50px;font-weight:600;color:var(--ink);letter-spacing:-1px;line-height:1}

.social{left:920px;top:10px;display:flex;flex-direction:column;gap:8px}
.social span{width:20px;height:20px;border:1.5px solid #bbb;border-radius:50%;display:block}

.search{left:763px;top:64px;width:186px;height:24px;display:flex}
.search input{flex:1;border:1px solid #ccc;font:11px "Open Sans",sans-serif;padding:0 8px;color:#999}
.search button{width:24px;background:var(--red);border:0;display:flex;align-items:center;justify-content:center}

.panel{left:257px;top:120px;width:691px;height:822px;background:var(--panel);border-radius:14px;
  box-shadow:0 2px 10px rgba(0,0,0,.12)}

.nav{left:257px;top:144px;width:691px;display:flex;justify-content:center;font-size:13px;color:#666;text-transform:uppercase}
.nav a{padding:6px 18px;color:inherit;text-decoration:none;border-left:1px solid var(--line)}
.nav a:first-child{border-left:0;color:var(--red)}
.nav-rule{left:276px;top:187px;width:650px;height:1px;background:var(--line)}

.hero{left:276px;top:202px;width:648px;height:256px;overflow:hidden}
.hero-photo{position:absolute;inset:0;background:linear-gradient(90deg,var(--hero-a) 0,#8ea6b2 45%,var(--hero-b) 75%,#dfe8ec 100%)}
.hero-copy{position:absolute;left:31px;top:48px;color:#fff;line-height:1.05}
.hero-copy .l1{font-size:31px;font-weight:300}
.hero-copy .l2{font-size:32px;font-weight:700}
.hero-copy .l3{font-size:34px;font-weight:700;color:var(--red)}
.hero-btn{position:absolute;left:31px;top:154px;background:var(--red);color:#fff;font-size:10px;font-weight:600;padding:4px 8px}
.hero-curve{position:absolute;left:0;bottom:0;width:648px;height:40px}

.dots{left:576px;top:470px;display:flex;gap:6px}
.dots span{width:10px;height:10px;border-radius:50%;background:#ccc}
.dots span:first-child{background:var(--red)}

.callout{left:257px;top:510px;width:691px;text-align:center;font-size:22px;color:#555}
.callout b{color:var(--red);font-weight:600}

.card{top:578px;width:197px}
.card h3{background:var(--red);color:#fff;font-size:16px;font-weight:400;text-align:center;height:40px;line-height:40px;text-transform:uppercase}
.card-photo{height:120px;background:linear-gradient(160deg,#9fb4c6,#5d7a92)}
.card-photo.micro{background:linear-gradient(160deg,#f1f3f5,#8b96a1)}
.card-photo.lab{background:linear-gradient(160deg,#c9dcf0,#6e93bd)}
.card p{font-size:10px;color:var(--muted);line-height:1.5;padding:16px 18px 0}
.card .more{display:inline-block;margin:18px 0 0 18px;background:var(--btn);color:#fff;font-size:10px;padding:5px 14px}

.panel-curve{left:257px;top:896px;width:691px;height:46px}

.footer{left:0;top:972px;width:1200px;height:228px;background:var(--footer);border-top:6px solid var(--red);color:var(--footer-text)}
.reps{position:absolute;left:254px;top:46px}
.reps h4{font-size:17px;font-weight:400;letter-spacing:.5px;background:#333;border:1px solid #666;padding:2px 8px;display:inline-block}
.reps ul{list-style:none;margin-top:12px;font-size:10px;line-height:1.9;text-transform:uppercase}
.reps li::before{content:"";display:inline-block;width:6px;height:6px;border-radius:50%;background:var(--red);margin-right:7px}
.contact{position:absolute;left:600px;top:40px;width:160px}
.contact h4{font-size:18px;font-weight:400;margin-bottom:10px}
.contact dt{font-size:10px;font-weight:700}
.contact dd{font-size:9px;color:#bbb;margin-bottom:4px}
.divider{position:absolute;left:764px;top:40px;width:1px;height:150px;background:#666}
.top-btn{position:absolute;left:836px;top:48px;width:72px;height:72px;border:2px solid #777;border-radius:50%;color:#999;font-size:14px;text-align:center;padding-top:30px}
.top-btn svg{position:absolute;left:27px;top:12px}
.legal{position:absolute;left:790px;top:128px;width:140px;text-align:center;font-size:9px;line-height:1.55}
.legal b{font-weight:700}
.legal .year{margin-top:8px;font-weight:700}
</style>
</head>
<body>

<div class="abs brand"><span class="brand-dot"></span><span class="brand-name">vitralis</span></div>

<div class="abs social" aria-label="redes sociais"><span></span><span></span></div>

<form class="abs search">
  <input type="text" value="Buscar" aria-label="Buscar">
  <button type="button" aria-label="buscar">
    <svg width="12" height="12" viewBox="0 0 12 12"><circle cx="5" cy="5" r="3.5" fill="none" stroke="#fff" stroke-width="1.5"/><line x1="7.6" y1="7.6" x2="11" y2="11" stroke="#fff" stroke-width="1.5"/></svg>
  </button>
</form>

<div class="abs panel"></div>

<nav class="abs nav">
  <a>Home</a><a>Quem somos</a><a>Produtos</a><a>Catálogos</a><a>Representantes</a><a>Fale conosco</a>
</nav>
<div class="abs nav-rule"></div>

<section class="abs hero">
  <div class="hero-photo" role="img" aria-label="Mão com luva segurando tubo de ensaio com líquido azul"></div>
  <div class="hero-copy">
    <div class="l1">EXPERT NO</div>
    <div class="l2">DIAGNÓSTICO DE</div>
    <div class="l3">COAGULOPATIAS</div>
  </div>
  <span class="hero-btn">SAIBA MAIS</span>
  <svg class="hero-curve" viewBox="0 0 648 40" preserveAspectRatio="none"><path d="M0 0 Q324 60 648 0 L648 40 L0 40 Z" fill="#fff"/></svg>
</section>

<div class="abs dots"><span></span><span></span><span></span><span></span></div>

<div class="abs callout">LIGUE GRÁTIS: <b>0800 000 0000</b></div>

<article class="abs card" style="left:295px">
  <h3>Laboratórios</h3>
  <div class="card-photo" role="img" aria-label="Profissional de laboratório com frasco de vidro"></div>
  <p>Equipamentos modernos para análises clínicas, com suporte técnico e treinamento em todo o país.</p>
  <span class="more">MAIS</span>
</article>
<article class="abs card" style="left:504px">
  <h3>Hemocentros</h3>
  <div class="card-photo micro" role="img" aria-label="Microscópio sobre bancada"></div>
  <p>Soluções completas para coleta, análise e armazenamento com qualidade e segurança garantidas.</p>
  <span class="more">MAIS</span>
</article>
<article class="abs card" style="left:713px">
  <h3>Hospitais</h3>
  <div class="card-photo lab" role="img" aria-label="Pesquisador com tubos de amostra em laboratório"></div>
  <p>Tecnologia confiável para rotinas hospitalares, com assistência rápida e atendimento dedicado.</p>
  <span class="more">MAIS</span>
</article>

<svg class="abs panel-curve" viewBox="0 0 691 46" preserveAspectRatio="none"><path d="M0 6 Q345 40 691 6" fill="none" stroke="#e6e6e6" stroke-width="2"/></svg>

<footer class="abs footer">
  <div class="reps">
    <h4>REPRESENTANTE AUTORIZADO</h4>
    <ul>
      <li>Lumeris Corporation</li>
      <li>Kalvix</li>
      <li>Nortec Diagnóstica</li>
    </ul>
  </div>
  <div class="contact">
    <h4>CONTATO</h4>
    <dl>
      <dt>Geral</dt><dd>contato@vitralis-exemplo.com.br</dd>
      <dt>Comercial</dt><dd>comercial@vitralis-exemplo.com.br</dd>
      <dt>Geral</dt><dd>0800 000 0000</dd>
      <dt>Comercial</dt><dd>+55 (41) 3000-0000</dd>
    </dl>
  </div>
  <div class="divider"></div>
  <div class="top-btn"><svg width="16" height="10" viewBox="0 0 16 10"><path d="M1 9 L8 2 L15 9" fill="none" stroke="#999" stroke-width="2"/></svg>TOP</div>
  <div class="legal">
    <b>Distribuidor no Brasil</b><br>
    Vitralis Equipamentos Hospitalares<br>
    T: (41) 3000-0000<br>
    F: (41) 3000-0001
    <div class="year">VITRALIS © 2024</div>
  </div>
</footer>

</body>
</html>
```